"Orvana" - Ketamine Clinic - Save Minds and Heal Hearts!! -

I need a very nice modern happy brain themed warm website design for our cutting edge modern and caring ketamine IV infusion clinic that also offers talk therapy and telemedicine visits.
A great design using the color schemes in out logos (grey, white, purples and that need metallic fading colored effect in the logo).

```html
<!DOCTYPE html>
<html lang="en">
<head>
<meta charset="utf-8">
<title>Orvana – Ketamine Clinic</title>
<link href="https://fonts.googleapis.com/css2?family=Catamaran:wght@500;600;700;800&family=Raleway:wght@400;500;600&display=swap" rel="stylesheet">
<style>
:root{
  --purple:#5a0fd6;
  --purple-deep:#4a08c0;
  --violet:#8b4be6;
  --cyan:#16c2e6;
  --dark:#3b3b3b;
  --ink:#111;
  --text:#333;
  --grey-band:#f2f2f2;
  --hero-bg:#ececec;
  --white:#fff;
}
*{box-sizing:border-box;margin:0;padding:0}
html,body{width:1200px;height:3279px;overflow:hidden}
body{position:relative;font-family:"Raleway",sans-serif;color:var(--text);background:var(--white)}
.abs{position:absolute}
h1,h2,h3,.heading{font-family:"Catamaran",sans-serif;color:var(--ink)}
.btn{position:absolute;display:flex;align-items:center;justify-content:center;font-family:"Catamaran",sans-serif;font-weight:700;color:var(--white);text-transform:uppercase;border-radius:5px}
.btn-purple{background:var(--purple)}
.btn-dark{background:var(--dark)}

/* header */
.hero{position:absolute;left:0;top:0;width:1200px;height:727px;background:radial-gradient(circle at 80% 45%,#fafafa 0%,var(--hero-bg) 70%)}
.hero-photo{position:absolute;left:0;top:0}
.topbar-email{position:absolute;left:720px;top:22px;display:flex;align-items:center;gap:14px}
.icon-circle{width:42px;height:42px;border-radius:50%;background:var(--purple);display:flex;align-items:center;justify-content:center}
.topbar-email b{display:block;font-family:"Catamaran",sans-serif;font-size:17px;font-weight:700;color:var(--ink);line-height:1.1}
.topbar-email span{font-size:13px;color:#222}
.nav{position:absolute;left:280px;top:87px;width:920px;height:53px;display:flex}
.nav-links{width:595px;background:#555;display:flex;align-items:center;padding-left:108px;gap:29px}
.nav-links a{color:var(--white);text-decoration:none;font-size:15px;font-weight:500}
.nav-phone{flex:1;background:var(--purple);display:flex;align-items:center;padding-left:50px;font-family:"Catamaran",sans-serif;font-weight:700;font-size:20px;color:var(--white);position:relative}
.phone-bubble{position:absolute;left:-8px;top:7px;width:40px;height:40px;border-radius:50%;background:var(--white);border:2px solid #ddd;display:flex;align-items:center;justify-content:center}
.logo-disc{position:absolute;left:118px;top:17px;width:174px;height:174px;border-radius:50%;background:var(--white);display:flex;align-items:center;justify-content:center;gap:8px}
.logo-disc span{font-family:"Catamaran",sans-serif;font-weight:800;font-size:32px;color:#555}
.logo-dot{width:18px;height:18px;border-radius:50%;background:var(--purple)}
.hero h1{position:absolute;left:560px;top:395px;width:570px;text-align:center;font-size:66px;font-weight:800;line-height:66px;letter-spacing:1px}

/* about */
.about h2{position:absolute;left:106px;top:856px;font-size:37px;font-weight:700}
.about p{position:absolute;left:106px;top:911px;width:478px;font-size:16.5px;line-height:30px;color:#222}

/* services */
.services{position:absolute;left:0;top:1363px;width:1200px;height:700px;background:var(--grey-band)}
.section-title{position:absolute;left:0;width:1200px;text-align:center;font-size:37px;font-weight:700;color:var(--ink);font-family:"Catamaran",sans-serif}
.card-img{position:absolute;top:154px;width:276px;height:276px;border-radius:3px}
.card-arrow{position:absolute;top:407px;width:54px;height:54px;border-radius:50%;background:var(--purple);display:flex;align-items:center;justify-content:center}
.card-title{position:absolute;top:478px;width:330px;text-align:center;font-family:"Catamaran",sans-serif;font-weight:600;font-size:24px;color:var(--ink)}

/* contact */
.contact-lead{position:absolute;left:123px;top:2226px;font-size:28px;font-weight:700}
.contact-text{position:absolute;left:119px;top:2272px;width:290px;font-size:16px;line-height:26px;color:#222}
.contact-item{position:absolute;left:118px;display:flex;align-items:center;gap:15px}
.ring{width:50px;height:50px;border-radius:50%;border:2px solid #444;display:flex;align-items:center;justify-content:center}
.contact-item b{display:block;font-family:"Catamaran",sans-serif;font-size:22px;font-weight:700;color:var(--ink);line-height:1.2}
.contact-item span{font-size:14px;color:#222}
.field{position:absolute;background:var(--white);box-shadow:0 2px 10px rgba(0,0,0,.06);font-size:15px;color:#888;padding:16px 24px}

/* cta */
.cta{position:absolute;left:0;top:2615px;width:1200px;height:211px;background:linear-gradient(90deg,#5d1bd6 0%,#4a5fe0 55%,var(--cyan) 100%)}
.cta h2{position:absolute;left:110px;top:46px;font-size:45px;line-height:51px;font-weight:700;color:var(--white)}
.cta p{position:absolute;left:391px;top:62px;width:460px;font-size:14.5px;line-height:31px;color:var(--white)}
.cta-phone{position:absolute;left:878px;top:74px;width:219px;height:42px;background:var(--purple);border-radius:4px;color:var(--white);font-family:"Catamaran",sans-serif;font-weight:700;font-size:20px;display:flex;align-items:center;padding-left:58px}
.cta-phone .phone-bubble{left:-2px;top:-4px;width:50px;height:50px}

/* footer */
.footer{position:absolute;left:0;top:2826px;width:1200px;height:453px;background:#fafafa}
.footer h3{position:absolute;font-size:22px;font-weight:700}
.help-list{position:absolute;left:129px;top:160px;list-style:none}
.help-list li{font-size:15px;line-height:30px;color:#222}
.help-list li::before{content:"«";color:var(--purple);margin-right:9px}
.footer-brand{position:absolute;left:425px;top:150px;width:270px;display:flex;align-items:center;justify-content:center;gap:14px}
.footer-brand span{font-family:"Catamaran",sans-serif;font-weight:800;font-size:64px;color:#555}
.footer-brand i{width:34px;height:34px;border-radius:50%;background:var(--purple);display:block}
.social{position:absolute;top:294px;width:30px;height:30px;border-radius:50%}
.copyright{position:absolute;left:0;top:393px;width:1200px;text-align:center;font-size:15px;color:#222}
.copyright u{color:var(--purple)}
</style>
</head>
<body>

<!-- hero -->
<section class="hero">
  <svg class="hero-photo" width="700" height="700" viewBox="0 0 700 700" role="img" aria-label="Nurse setting up an IV infusion for a relaxed patient, framed in a flower-shaped purple and teal overlay with white blossoms">
    <defs>
      <linearGradient id="heroGrad" x1="0" y1="0" x2="1" y2="0.6">
        <stop offset="0" stop-color="#8a3be0"/>
        <stop offset="0.55" stop-color="#6d4ed6"/>
        <stop offset="1" stop-color="#3fb4c9"/>
      </linearGradient>
    </defs>
    <path d="M0 0 H620 C690 40 700 140 640 190 C700 240 690 330 610 350 C620 430 560 480 480 470 C470 560 380 610 300 560 C280 640 170 650 150 560 C90 560 40 520 0 470 Z" fill="url(#heroGrad)"/>
  </svg>

  <div class="logo-disc"><i class="logo-dot"></i><span>Orvana</span></div>

  <div class="topbar-email">
    <div class="icon-circle">
      <svg width="20" height="16" viewBox="0 0 20 16"><rect x="1" y="1" width="18" height="14" rx="2" fill="#fff"/><path d="M2 3 L10 9 L18 3" stroke="#5a0fd6" stroke-width="2" fill="none"/></svg>
    </div>
    <div><b>SEND US EMAIL</b><span>info@orvana-care.com</span></div>
  </div>
  <div class="btn btn-purple" style="left:956px;top:25px;width:130px;height:36px;font-size:14px;">Book Now</div>

  <nav class="nav">
    <div class="nav-links">
      <a>Home</a><a>About</a><a>Treatments</a><a>Resources</a><a>Contact Us</a>
    </div>
    <div class="nav-phone">
      <div class="phone-bubble">
        <svg width="18" height="18" viewBox="0 0 24 24"><path d="M6.6 10.8a15 15 0 006.6 6.6l2.2-2.2a1 1 0 011-.25 11.4 11.4 0 003.6.57 1 1 0 011 1V20a1 1 0 01-1 1A17 17 0 013 4a1 1 0 011-1h3.5a1 1 0 011 1c0 1.25.2 2.45.57 3.57a1 1 0 01-.25 1z" fill="#5a0fd6"/></svg>
      </div>
      +1 555 010 2040
    </div>
  </nav>

  <h1>SAVE MINDS AND HEAL HEARTS!!</h1>
  <div class="btn btn-purple" style="left:722px;top:560px;width:255px;height:44px;font-size:17px;">Appointment Today</div>
</section>

<!-- about -->
<section class="about">
  <h2>ABOUT US</h2>
  <p>Lorem ipsum dolor sit amet, consectetur adipiscing elit, sed do eiusmod tempor incididunt ut labore et dolore magna aliqua. Quis ipsum suspendisse ultrices gravida. Risus commodo viverra maecenas accumsan lacus vel facilisis. Lorem ipsum dolor sit amet, consectetur adipiscing elit, sed do eiusmod tempor incididunt ut labore et dolore magna aliqua. Quis ipsum suspendisse ultrices gravida. Risus commodo viverra maecenas accumsan lacus vel facilisis.</p>
  <div class="btn btn-dark" style="left:108px;top:1174px;width:186px;height:49px;font-size:17px;">Learn More</div>

  <svg class="abs" style="left:615px;top:818px" width="494" height="446" viewBox="0 0 494 446">
    <g fill="var(--purple-deep)">
      <circle cx="168" cy="100" r="100"/>
      <circle cx="326" cy="100" r="100"/>
      <circle cx="168" cy="346" r="100"/>
      <circle cx="326" cy="346" r="100"/>
      <circle cx="100" cy="223" r="100"/>
      <circle cx="394" cy="223" r="100"/>
    </g>
    <defs>
      <linearGradient id="aboutGrad" x1="0" y1="0" x2="1" y2="1">
        <stop offset="0" stop-color="#e9e6e0"/>
        <stop offset="0.5" stop-color="#9fc6e4"/>
        <stop offset="1" stop-color="#d8cfc2"/>
      </linearGradient>
    </defs>
    <circle cx="247" cy="223" r="208" fill="url(#aboutGrad)" role="img" aria-label="Smiling patient giving a thumbs up while receiving an IV infusion in a bright clinic room"/>
    <circle cx="252" cy="223" r="23" fill="var(--purple)"/>
    <path d="M246 213 L260 223 L246 233 Z" fill="#fff"/>
  </svg>
</section>

<!-- services -->
<section class="services">
  <div class="section-title" style="top:60px;">OUR SERVICES</div>

  <div class="card-img" style="left:140px;background:linear-gradient(135deg,#f2f2f0,#dcdad6);" role="img" aria-label="Patient relaxing in a white infusion chair during a ketamine infusion"></div>
  <div class="card-img" style="left:463px;background:linear-gradient(135deg,#c9d3dc,#5c7fa8 55%,#2a2f3a);" role="img" aria-label="Doctor and colleague reviewing notes on a tablet"></div>
  <div class="card-img" style="left:785px;background:linear-gradient(135deg,#d9e6ef,#6f9fcf 45%,#c9b7a6);" role="img" aria-label="Gloved hand holding a medicine vial and syringe"></div>

  <div class="card-arrow" style="left:251px"><svg width="24" height="24" viewBox="0 0 24 24"><path d="M4 12h15M13 6l6 6-6 6" stroke="#fff" stroke-width="2.6" fill="none" stroke-linecap="round" stroke-linejoin="round"/></svg></div>
  <div class="card-arrow" style="left:574px"><svg width="24" height="24" viewBox="0 0 24 24"><path d="M4 12h15M13 6l6 6-6 6" stroke="#fff" stroke-width="2.6" fill="none" stroke-linecap="round" stroke-linejoin="round"/></svg></div>
  <div class="card-arrow" style="left:897px"><svg width="24" height="24" viewBox="0 0 24 24"><path d="M4 12h15M13 6l6 6-6 6" stroke="#fff" stroke-width="2.6" fill="none" stroke-linecap="round" stroke-linejoin="round"/></svg></div>

  <div class="card-title" style="left:113px">Ketamine Infusions</div>
  <div class="card-title" style="left:436px">Clinic Consulting</div>
  <div class="card-title" style="left:758px">Ketamine Knowledge</div>

  <div class="btn btn-dark" style="left:505px;top:566px;width:189px;height:55px;font-size:20px;">View More</div>
</section>

<!-- contact -->
<section class="contact">
  <div class="section-title" style="top:2133px;">CONTACT US</div>
  <h3 class="contact-lead">GET IN TOUCH</h3>
  <p class="contact-text">Lorem ipsum dolor sit amet, consectetur adipiscing elit, sed do eiusmod tempor incididunt</p>

  <div class="contact-item" style="top:2382px">
    <div class="ring"><svg width="18" height="18" viewBox="0 0 24 24"><path d="M6.6 10.8a15 15 0 006.6 6.6l2.2-2.2a1 1 0 011-.25 11.4 11.4 0 003.6.57 1 1 0 011 1V20a1 1 0 01-1 1A17 17 0 013 4a1 1 0 011-1h3.5a1 1 0 011 1c0 1.25.2 2.45.57 3.57a1 1 0 01-.25 1z" fill="#5a0fd6"/></svg></div>
    <div><b>Phone</b><span>+1 555 010 2040</span></div>
  </div>
  <div class="contact-item" style="top:2470px">
    <div class="ring"><svg width="18" height="14" viewBox="0 0 20 16"><rect x="1" y="1" width="18" height="14" rx="2" fill="#5a0fd6"/><path d="M2 3 L10 9 L18 3" stroke="#fff" stroke-width="2" fill="none"/></svg></div>
    <div><b>Email</b><span>info@orvana-care.com</span></div>
  </div>

  <div class="field" style="left:441px;top:2231px;width:317px;height:53px;">Name</div>
  <div class="field" style="left:441px;top:2298px;width:317px;height:54px;">Phone</div>
  <div class="field" style="left:441px;top:2367px;width:317px;height:52px;">Email</div>
  <div class="btn btn-dark" style="left:441px;top:2437px;width:317px;height:51px;font-size:16px;">Submit</div>
  <div class="field" style="left:779px;top:2231px;width:318px;height:257px;">Type your message</div>
</section>

<!-- call to action -->
<section class="cta">
  <h2>NEED HELP?<br>CONTACT US</h2>
  <p>Lorem ipsum dolor sit amet, consectetur adipiscing elit, sed do eiusmod tempor incididunt ut labore et dolore magna aliqua. Quis ipsum suspendisse ultrices gravida.</p>
  <div class="cta-phone">
    <div class="phone-bubble">
      <svg width="18" height="18" viewBox="0 0 24 24"><path d="M6.6 10.8a15 15 0 006.6 6.6l2.2-2.2a1 1 0 011-.25 11.4 11.4 0 003.6.57 1 1 0 011 1V20a1 1 0 01-1 1A17 17 0 013 4a1 1 0 011-1h3.5a1 1 0 011 1c0 1.25.2 2.45.57 3.57a1 1 0 01-.25 1z" fill="#5a0fd6"/></svg>
    </div>
    +1 555 010 2040
  </div>
</section>

<!-- footer -->
<footer class="footer">
  <h3 style="left:129px;top:120px;">HELP LINKS</h3>
  <ul class="help-list">
    <li>Terms &amp; Conditions</li>
    <li>Privacy Policy</li>
    <li>About Us</li>
    <li>Support</li>
  </ul>

  <div class="footer-brand"><i></i><span>Orvana</span></div>

  <h3 style="left:747px;top:120px;">GET OUR NEWSLETTER</h3>
  <div class="field" style="left:747px;top:167px;width:337px;height:42px;border:1px solid #aaa;box-shadow:none;font-size:12px;padding:12px 16px;">Enter Your Email</div>
  <div class="btn btn-purple" style="left:747px;top:220px;width:337px;height:42px;font-size:15px;">Subscribe Now</div>
  <div class="social" style="left:755px;background:var(--purple)"></div>
  <div class="social" style="left:792px;background:#9a9a9a"></div>
  <div class="social" style="left:828px;background:#9a9a9a"></div>

  <div class="copyright">©Copyrights 2023 &nbsp;<u>Orvana-care.com</u> | &nbsp;&nbsp;All Rights Reserved</div>
</footer>

</body>
</html>
```